Brochure to advertise our unique physiotherapy clinic to general practitioners

We want to advertise our unique physiotherapy clinic to general practitioners (GPs) to develop there awareness of both our existence and services offered. The brochure should highlight our uniqueness (i.e. providing the highest quality care, advice and education) based on our expert research-based knowledge and skills. After reading the brochure, we want GPs to feel like they know us a little and feel happy to refer their patients to our clinic.
Attached is a draft flyer containing our logo, contact details, profile pictures and the information we would like to be contained in the brochure. We would like the brochure to be A4 double sided and able to be folded to fit into an envelope. More material (pictures) and understanding of our clinic can be found at www.kinetreva.com.au

A brief background of our team:
Our team currently consists of two physiotherapists specialising in the management of musculoskeletal and sports injuries, Dr Howard Tenniscombe and Dr Lionel Fairweather. Both Howard and Lionel have completed PhDs related to musculosketal injury management, and continue to be actively involved in international research groups. Between them they have authored more than 50 peer reviewed papers, presented at countless national and international conferences, and coordinate numerous courses to facilitate professional development of other clinicians. Most importantly, they continue to enjoy mixing these research and teaching activities with treating patients.

Updates
Project Deadline Extended
Reason: Consultation with clinic partner is needed and to allow time for modifications and additional designs. We will pick one, just want quality.
Thanks

Project Deadline Extended

Thank you for some great designs thus far everyone. We have decided to remove the fees from the brochure so please do the same for any future submissions. In the process of trying to provide feedback now.
Thanks
Project Deadline Extended
Reason: A couple of designs are close and we want to allow time to make appropriate modifications. This will be the last extension. Thanks for everyones effort so far

Project Deadline Extended

Target Market(s)
Australian General Practitioners and other health professionals are the targeted audience
Industry/Entity Type
Clinic
Look and feel

```html
<!DOCTYPE html>
<html lang="en">
<head>
<meta charset="utf-8">
<title>Kinetreva brochure spreads</title>
<link href="https://fonts.googleapis.com/css2?family=Questrial&family=Didact+Gothic&display=swap" rel="stylesheet">
<style>
  :root{
    --page:#ffffff;
    --sky-top:#1f6fd0;
    --sky-mid:#6fa9e8;
    --sky-low:#dfeefb;
    --grass:#5fb51f;
    --grass-dark:#2f7d10;
    --spread-blue:#1c6fd9;
    --spread-deep:#0d52b8;
    --lime:#9ad80f;
    --lime-dark:#6aa800;
    --ink:#1a1a1a;
    --white:#ffffff;
    --brand-blue:#1f4fa3;
  }
  *{box-sizing:border-box;margin:0;padding:0}
  html,body{width:1200px;height:900px;overflow:hidden;background:var(--page)}
  body{position:relative;font-family:"Questrial",sans-serif;color:var(--white)}

  .spread{position:absolute;top:130px;width:549px;height:388px;overflow:hidden}

  /* cover spread */
  .cover{left:43px}
  .cover-sky{position:absolute;left:0;top:0;width:549px;height:300px;background:linear-gradient(180deg,var(--sky-top) 0%,var(--sky-mid) 45%,var(--sky-low) 100%)}
  .cover-grass{position:absolute;left:0;bottom:0;width:549px;height:100px;background:linear-gradient(180deg,#8fd23a 0%,var(--grass) 45%,var(--grass-dark) 100%)}
  .cover-tagline{position:absolute;left:304px;top:62px;font-family:"Didact Gothic",sans-serif;font-size:13px;line-height:14px;color:rgba(255,255,255,.8);letter-spacing:.2px}
  .cover-address{position:absolute;left:2px;top:265px;width:158px;height:46px;background:var(--white);color:var(--ink);font-size:7px;line-height:9px;padding:3px 0 0 38px;box-shadow:0 2px 4px rgba(0,0,0,.25);font-style:normal}
  .cover-brand{position:absolute;left:297px;top:260px;width:166px;height:50px;background:var(--white);display:flex;align-items:center;gap:8px;padding-left:10px;box-shadow:0 2px 4px rgba(0,0,0,.25)}
  .brand-dot{width:22px;height:22px;border-radius:50%;background:var(--brand-blue)}
  .brand-name{font-size:22px;color:var(--brand-blue);line-height:1}

  /* inside spread */
  .inside{left:615px;background:linear-gradient(135deg,var(--spread-blue) 0%,#2b82ea 55%,var(--spread-deep) 100%)}
  .tab{position:absolute;height:16px;background:var(--lime);color:var(--ink);font-size:9px;line-height:16px;padding:0 8px;text-transform:uppercase}
  .tab::before{content:"";position:absolute;left:-8px;top:-6px;width:12px;height:12px;background:var(--lime-dark)}
  .copy{position:absolute;font-size:6.8px;line-height:8.6px;text-align:justify;color:var(--white)}
  .portrait{position:absolute;left:191px;width:64px;height:48px;border:2px solid #9cc6f5;background:linear-gradient(180deg,#cfd7df,#6d7e90)}
  .portrait-name{position:absolute;left:178px;width:90px;font-size:5px;text-align:center;text-transform:uppercase;white-space:nowrap}
  .heading-right{position:absolute;left:290px;top:13px;font-size:10px;font-weight:400;letter-spacing:.2px;text-transform:uppercase}
  .treat-photos{position:absolute;left:290px;top:30px;width:224px;height:60px;display:flex;gap:3px;background:var(--white);padding:2px}
  .treat-photos div{flex:1;background:linear-gradient(135deg,#f3d7c2,#c99779)}
  .conditions{position:absolute;top:117px;list-style:none;font-size:6.8px;line-height:8px;color:#e8f8b0}
  .conditions li{padding-left:8px;position:relative;white-space:nowrap}
  .conditions li::before{content:"";position:absolute;left:0;top:2px;width:4px;height:4px;background:var(--lime)}
  .exercise-photo{position:absolute;left:270px;top:230px;width:279px;height:158px;background:linear-gradient(160deg,rgba(43,130,234,0) 0%,#8a7fb0 55%,#c79a82 100%)}
  .partner-badge{position:absolute;left:453px;top:362px;width:58px;height:18px;background:var(--white);border:1px solid var(--lime-dark)}
</style>
</head>
<body>

<section class="spread cover" aria-label="Brochure cover spread">
  <div class="cover-sky" role="img" aria-label="Photo of a woman leaping through a cloudy blue sky holding a flowing colourful scarf"></div>
  <div class="cover-grass" role="img" aria-label="Green grass meadow under the clouds"></div>
  <p class="cover-tagline">Successfully treating<br>difficult injuries</p>
  <address class="cover-address">
    Meridian Fitness, Level 4, The Atrium<br>
    22-24 Larkin Ave, Brookvale, 3127<br>
    e: info@kinetreva.com.au<br>
    w: www.kinetreva.com.au<br>
    p: 9000 4170
  </address>
  <div class="cover-brand"><span class="brand-dot"></span><span class="brand-name">Kinetreva</span></div>
</section>

<section class="spread inside" aria-label="Brochure inside spread">
  <div class="tab" style="left:18px;top:20px">The Clinic</div>
  <p class="copy" style="left:18px;top:40px;width:240px">We are a very unique and progressive physiotherapy clinic at Kinetreva. Our clinic is located within Meridian Fitness, Level 4, 22-24, Larkin Avenue, Brookvale, VIC, 3127. Further information about us is detailed below. Additionally, please visit our website and join the associated 'tendinopathy' 'patellofemoral' and 'biomechanics' blogs if you are interested at: http://www.kinetreva.com.au/</p>

  <div class="tab" style="left:18px;top:108px">Who are we?</div>
  <p class="copy" style="left:18px;top:133px;width:170px;font-size:6.3px;line-height:8px">Our team currently consists of two physiotherapists specialising in the management of musculoskeletal and sports injuries, Dr Howard Tenniscombe and Dr Lionel Fairweather. Both Howard and Lionel have completed PhDs related to musculoskeletal injury management, and continue to be actively involved in international research groups. Between them they have authored more than 40 peer reviewed papers, presented at countless national and international conferences, and coordinate numerous courses to facilitate professional development of other clinicians. Most importantly, they continue to enjoy mixing these research and teaching activities with treating patients.</p>
  <div class="portrait" style="top:134px" role="img" aria-label="Portrait of Dr Howard Tenniscombe"></div>
  <p class="portrait-name" style="top:184px">Dr Howard Tenniscombe</p>
  <div class="portrait" style="top:192px" role="img" aria-label="Portrait of Dr Lionel Fairweather"></div>
  <p class="portrait-name" style="top:242px">Dr Lionel Fairweather</p>

  <div class="tab" style="left:18px;top:258px">Services Offered</div>
  <p class="copy" style="left:18px;top:278px;width:240px;font-size:6.6px;line-height:8.4px">All patients receive the highest quality 1-1 physiotherapy treatment and we offer patients accurate, realistic and lasting solution to their problems. We can guarantee the quality of our treatment because we are genuine experts in managing difficult injuries, with a wealth of clinical and research experience. This ultimately means we can more effective care, saving patients both time and money. We have the facilities, knowledge and skills to complete comprehensive biomechanical assessments, evidence based exercise prescription, access to a full gym, highly effective manual therapy techniques, dry needling, diagnostic ultrasound, shockwave therapy, and foot orthoses advice/prescription. Put together, this will ensure all patients who attend our clinic an optimal recovery from almost any musculoskeletal injury, whether acute or chronic.</p>

  <h2 class="heading-right">We treat injuries others cannot fix</h2>
  <div class="treat-photos" role="img" aria-label="Three photos of hands-on physiotherapy treatment on leg, foot and hand">
    <div></div><div></div><div></div>
  </div>
  <p class="copy" style="left:290px;top:95px;width:240px;text-align:left">We have a reputation for successfully managing injuries that are difficult, or unresolving, including:</p>
  <ul class="conditions" style="left:288px">
    <li>Achilles tendinopathy</li><li>Patellar tendinopathy</li><li>Tennis elbow</li><li>Rotator cuff injury</li><li>Hamstring origin tendinopathy</li><li>Tibialis posterior tendon injury</li><li>Plantar fasciitis</li><li>Iliotibial band syndrome</li>
  </ul>
  <ul class="conditions" style="left:416px">
    <li>Patellofemoral joint injury</li><li>Back and neck pain</li><li>Chronic strains and sprains</li><li>Shoulder pain</li><li>Groin pain</li><li>Hip impingement</li><li>Stress fractures</li><li>Shin splints (exercise induced leg pain)</li>
  </ul>

  <div class="exercise-photo" role="img" aria-label="Photo of a trainer guiding a woman through sit-up exercises"></div>
  <div class="partner-badge"></div>
</section>

</body>
</html>
```